Financial Service Company Need Business Card Design

This is a new startup company, first of its kind to offer this service. We facilitate the movement of deposit funds electronically between home buyers and real estate brokerages.Our customers are REALTORS®, real estate brokerages, and home buyers, we identify ourselves as a financial/technology company.
Not looking for anything too flashy. Just a clean design that shows the logo, contact info, etc. Company colors can be seen on attached logo, and 'coming soon page'
www.plumvault.ca
Industry/Entity Type
Business
Contact Information for Business Card

```html
<!DOCTYPE html>
<html lang="en">
<head>
<meta charset="utf-8">
<title>PlumVault Business Card</title>
<link href="https://fonts.googleapis.com/css2?family=Saira:wght@500;600;700&display=swap" rel="stylesheet">
<style>
  :root {
    --backdrop: #e4e4e4;
    --brand-orange: #e9532b;
    --card-grey: #6a696b;
    --stripe-black: #050505;
    --ink-white: #ffffff;
  }
  * { margin: 0; padding: 0; box-sizing: border-box; }
  html, body {
    width: 1200px;
    height: 1000px;
    overflow: hidden;
    background: var(--backdrop);
    font-family: "Saira", Arial, sans-serif;
  }
  .canvas {
    position: relative;
    width: 1200px;
    height: 1000px;
  }
  .card {
    position: absolute;
    left: 285px;
    width: 630px;
    height: 380px;
    border-radius: 26px;
    overflow: hidden;
  }
  .card-front {
    top: 70px;
    background: var(--brand-orange);
    display: flex;
    align-items: center;
    justify-content: center;
  }
  .brand-name {
    color: var(--ink-white);
    font-weight: 600;
    letter-spacing: 0.5px;
    line-height: 1;
  }
  .card-front .brand-name { font-size: 72px; }
  .card-back {
    top: 540px;
    background: var(--card-grey);
    color: var(--ink-white);
  }
  .chip {
    position: absolute;
    left: 50px;
    top: 48px;
    width: 86px;
    height: 52px;
    border-radius: 8px;
    background: var(--brand-orange);
  }
  .back-brand {
    position: absolute;
    top: 34px;
    left: 190px;
    right: 30px;
    text-align: center;
  }
  .back-brand .brand-name { font-size: 40px; }
  .contact {
    position: absolute;
    top: 96px;
    left: 150px;
    right: 20px;
    text-align: center;
    font-weight: 700;
  }
  .contact-name { font-size: 25px; letter-spacing: 1px; line-height: 1.05; }
  .contact-title { font-size: 16px; letter-spacing: 1px; line-height: 1; margin-bottom: 10px; }
  .contact-line { font-size: 19px; letter-spacing: 1px; line-height: 1.35; }
  .contact-line .gap { display: inline-block; width: 26px; }
  .mag-stripe {
    position: absolute;
    left: 0;
    right: 0;
    top: 262px;
    height: 58px;
    background: var(--stripe-black);
  }
  .web-address {
    position: absolute;
    left: 0;
    right: 0;
    top: 328px;
    text-align: center;
    color: var(--brand-orange);
    font-weight: 700;
    font-size: 22px;
    letter-spacing: 3px;
    text-transform: uppercase;
  }
</style>
</head>
<body>
<main class="canvas">
  <section class="card card-front" aria-label="Card front">
    <span class="brand-name">PlumVault</span>
  </section>

  <section class="card card-back" aria-label="Card back">
    <div class="chip"></div>
    <div class="back-brand"><span class="brand-name">PlumVault</span></div>
    <div class="contact">
      <p class="contact-name">Jane Morgan</p>
      <p class="contact-title">Change</p>
      <p class="contact-line">jmorgan@plumvault.ca</p>
      <p class="contact-line">Phone&nbsp;&nbsp;123 456 789<span class="gap"></span>Mobile&nbsp;&nbsp;123 456 789</p>
      <p class="contact-line">123 Main Avenue<span class="gap"></span>Anytown</p>
    </div>
    <div class="mag-stripe"></div>
    <p class="web-address">www.plumvault.ca</p>
  </section>
</main>
</body>
</html>
```